Marketplace website landing pages
3D Printing Marketplace
Marketplace website landing pages  - Printing
Creative Brief
Printing
We require 3 No. Marketplace website landing pages mock-ups only. We will supply the main logo. The marketplace is for everything 3D printing. The site has two concepts one marketplace like Vornelli.com, Quibble, Tandoshop & plinko etc. where you buy products, but can also sell or open a shop on the platform. The other will be for services like Grivio & Menfra etc. the services will be 3D product / prototype design services, 3D printing of objects etc. buyers can place projects and service providers and freelancers can bid for the project. We need main landing page before the site splits in two, with links to products and services pages. Products landing page a mix of the best bit of Vornelli.com, Quibble, Tandoshop & Plinko etc. We also need things like – Select Language, shop by brand, multi county links like the bottom of the page on Vornelli.com, You do not need to worry too much about have the correct names in categories or photos etc., this is all about the layout and functions within the layout. Look at the landing pages of the sites listed. Services landing pages will have some of the same detail as the products landing page like search, sign-in, details at bottom of pages etc. otherwise you will think you have gone to different site. For this think freelancing like Grivio & menfra etc. again this is about the layout. Total pages layouts designs to be delivered: 3

```html
<!DOCTYPE html>
<html lang="en">
<head>
<meta charset="utf-8">
<title>Layerhub – 3D Printing Market</title>
<link href="https://fonts.googleapis.com/css2?family=Oxygen:wght@400;700&family=Roboto:wght@400;500;700&family=Russo+One&display=swap" rel="stylesheet">
<style>
:root{
  --black:#050505;
  --orange:#f47a1f;
  --orange-dark:#e0620c;
  --blue:#1f5fa6;
  --blue-bright:#2b8fd6;
  --blue-band:#1d5d9e;
  --blue-footer:#1c5a98;
  --grey-hero:#e4e4e4;
  --dark-text:#222;
}
*{box-sizing:border-box;margin:0;padding:0}
html,body{width:740px;height:1200px;overflow:hidden}
body{position:relative;background:#ececec;font-family:"Oxygen",sans-serif;color:var(--dark-text)}
.abs{position:absolute}

/* header */
.site-header{position:absolute;left:0;top:0;width:740px;height:75px;background:var(--black);border-bottom:1px solid var(--orange)}
.top-links{position:absolute;top:5px;left:375px;display:flex;align-items:center;gap:6px;font-size:8px;color:#ddd}
.top-links .sep{color:#666}
.top-links .ico{width:7px;height:8px;background:var(--blue-bright);border-radius:2px;display:inline-block;margin-right:3px;vertical-align:-1px}
.flag{width:16px;height:11px;display:inline-block}
.cart{color:var(--orange);margin-left:6px}
.cart b{color:#fff;font-weight:400}
.brand{position:absolute;left:76px;top:24px;display:flex;align-items:center;gap:6px}
.brand-dot{width:20px;height:20px;border-radius:50%;background:var(--orange)}
.brand-name{font-family:"Roboto",sans-serif;font-weight:700;font-size:23px;color:#3d86d6;line-height:1}
.brand-tag{position:absolute;left:154px;top:51px;font-family:"Roboto",sans-serif;font-weight:700;font-size:8px;letter-spacing:.6px;color:var(--orange)}
.main-nav{position:absolute;left:277px;top:45px;height:30px;display:flex;font-size:9.5px;letter-spacing:.5px;color:#eee}
.main-nav a{color:inherit;text-decoration:none;padding:0 5px;line-height:30px;border-right:1px solid #333}
.main-nav a.active{background:#2a2a2a;border-bottom:3px solid var(--orange);padding:0 7px;line-height:27px}

/* hero */
.hero{position:absolute;left:0;top:76px;width:740px;height:248px;background:var(--grey-hero)}
.brand-menu{position:absolute;left:81px;top:94px;width:145px}
.brand-menu h3{background:linear-gradient(#2f73c5,#1d58a3);color:#fff;font-family:"Roboto",sans-serif;font-weight:500;font-size:11.5px;padding:4px 9px;height:23px}
.brand-menu ul{list-style:none;background:#f4f4f4}
.brand-menu li{height:19px;line-height:19px;padding-left:9px;font-family:"Roboto",sans-serif;font-weight:500;font-size:7.5px;color:#555;border-bottom:1px dashed #ccc}
.search{position:absolute;left:81px;top:259px;width:145px;height:16px;display:flex;border:1px solid #ccc;background:#fff}
.search span{flex:1;font-family:"Roboto",sans-serif;font-size:7.5px;font-weight:500;line-height:14px;padding-left:9px}
.search i{width:20px;background:var(--blue)}
.printer-photo{position:absolute;left:265px;top:130px;width:220px;height:148px;border-radius:10px;background:linear-gradient(150deg,#b9bcc0,#6d7075 60%,#4b4d51)}
.hero-title{position:absolute;left:383px;top:100px;font-family:"Russo One",sans-serif;font-weight:400;font-size:24px;line-height:28px;color:var(--blue);letter-spacing:.3px}
.hero-points{position:absolute;left:497px;top:133px;list-style:none;font-family:"Roboto",sans-serif;font-size:11.5px;color:#333}
.hero-points li{height:19.6px;position:relative;padding-left:9px}
.hero-points li:before{content:"";position:absolute;left:0;top:4px;border-left:4px solid var(--orange);border-top:3px solid transparent;border-bottom:3px solid transparent}
.learn-more{position:absolute;left:496px;top:254px;width:102px;height:20px;background:linear-gradient(#f98f35,var(--orange-dark));color:#fff;font-family:"Roboto",sans-serif;font-weight:500;font-size:11px;line-height:20px;padding-left:6px}
.learn-more i{position:absolute;right:6px;top:5px;width:10px;height:10px;border-radius:50%;background:#fff}
.dots{position:absolute;left:496px;top:297px;display:flex;gap:4px}
.dots span{width:8px;height:8px;border-radius:50%;background:#999}
.dots span.on{background:var(--orange)}

/* feature band */
.features{position:absolute;left:0;top:324px;width:740px;height:115px;background:linear-gradient(#2a6db1,var(--blue-band));display:flex;padding:0 60px}
.feature{flex:1;text-align:center;color:#fff;border-right:1px solid rgba(255,255,255,.2);margin:16px 0 10px}
.feature:last-child{border:none}
.feature-icon{width:50px;height:50px;border-radius:50%;background:#fff;border:3px solid #cfd8e3;margin:-9px auto 0;display:flex;align-items:center;justify-content:center}
.feature h4{font-family:"Roboto",sans-serif;font-weight:700;font-size:11.5px;color:var(--orange);margin-top:6px}
.feature p{font-size:6.3px;line-height:8px;margin-top:3px}

/* promo cards */
.promo{position:absolute;top:452px;width:271px;height:131px;background:#fff;border:1px solid #ddd}
.promo h2{position:absolute;left:11px;top:15px;font-family:"Oxygen",sans-serif;font-weight:700;font-size:20px;line-height:22px;color:var(--blue)}
.promo h2 em{font-style:normal;color:var(--orange)}
.promo p{position:absolute;left:11px;top:70px;width:124px;font-size:7.5px;line-height:11px;color:#333}
.promo .btn{position:absolute;left:11px;top:103px;width:78px;height:17px;background:var(--blue-bright);color:#fff;font-weight:700;font-size:9.5px;line-height:17px;text-align:center}
.promo .photo{position:absolute}

/* featured */
.section-title{position:absolute;left:92px;top:606px;width:555px;height:14px;border-top:1px solid #ccc;margin-top:7px}
.section-title span{position:absolute;left:200px;top:-10px;background:#ececec;padding:0 8px;font-family:"Roboto",sans-serif;font-weight:500;font-size:13.5px;line-height:16px;color:var(--blue)}
.section-title span b{font-weight:500;color:var(--orange)}
.product{position:absolute;width:178px;height:160px;background:linear-gradient(#fafafa,#efefef)}
.product .photo{position:absolute;left:27px;top:9px;width:125px;height:84px;border:1px solid #ddd}
.product h5{position:absolute;left:27px;top:98px;font-family:"Oxygen",sans-serif;font-weight:700;font-size:8.5px;color:var(--blue)}
.product p{position:absolute;left:27px;top:110px;width:112px;font-size:7px;line-height:11px;color:#333}
.price-bar{position:absolute;left:27px;top:138px;width:116px;height:14px;background:#222;border-radius:2px;display:flex;align-items:center;font-size:7px;color:#fff}
.price-bar .price{color:var(--orange);font-weight:700;font-size:8px;width:50px;padding-left:8px;border-right:1px solid #666}
.price-bar .add{padding-left:6px;font-weight:700}
.arrow{position:absolute;width:14px;height:18px}

/* contact strip */
.divider{position:absolute;left:92px;top:970px;width:555px;height:1px;background:#d4d4d4}
.more-info{position:absolute;left:92px;top:980px;font-weight:700;font-size:20px;color:var(--blue-bright)}
.more-sub{position:absolute;left:92px;top:1006px;font-size:8.5px;color:#333}
.phone-number{position:absolute;left:325px;top:983px;font-size:21px;color:#555}
.contact-btn{position:absolute;left:491px;top:985px;width:156px;height:29px;background:var(--blue-bright);color:#fff;font-size:15px;line-height:29px;text-align:center}

/* footer */
.site-footer{position:absolute;left:0;top:1028px;width:740px;height:172px;background:var(--blue-footer);color:#e8f0f9}
.fcol{position:absolute;top:12px}
.fcol h4{font-family:"Roboto",sans-serif;font-weight:700;font-size:10.5px;color:#fff;margin-bottom:6px}
.fcol ul{list-style:none;font-size:7.8px;line-height:12.9px}
.fcol.countries ul{line-height:11.3px;display:inline-block;width:58px;vertical-align:top}
.alerts{position:absolute;left:497px;top:12px;width:150px}
.alerts .bell{position:absolute;left:0;top:2px;width:16px;height:16px;border-radius:50%;background:#f5a623}
.alerts h4{margin-left:22px;font-family:"Roboto",sans-serif;font-weight:400;font-size:10px;line-height:10px;color:#fff}
.alerts h4 b{font-weight:700}
.alerts p{font-size:8.3px;line-height:12px;margin-top:6px}
.signup{display:flex;gap:8px;margin-top:6px}
.signup span{width:96px;height:17px;background:#fff;font-size:6.5px;color:#999;line-height:17px;padding-left:4px}
.signup b{width:46px;height:17px;background:var(--blue-bright);font-size:7.5px;line-height:17px;text-align:center;color:#fff}
.social{display:flex;gap:6px;margin-top:11px}
.social span{width:16px;height:16px;font-size:6px;line-height:16px;text-align:center;color:#fff;font-weight:700}
.foot-line{position:absolute;left:92px;top:128px;width:555px;height:1px;background:rgba(255,255,255,.25)}
.payments{position:absolute;left:92px;top:142px;display:flex;align-items:center;gap:4px;font-family:"Roboto",sans-serif;font-size:11.5px;color:#fff}
.payments .label{margin-right:3px}
.pay{width:25px;height:14px;background:#fff;color:#1c5a98;font-size:4.6px;font-weight:700;line-height:14px;text-align:center;font-family:"Oxygen",sans-serif}
.copyright{position:absolute;left:431px;top:148px;font-size:7.5px;color:#fff}
</style>
</head>
<body>

<header class="site-header">
  <div class="top-links">
    <span><i class="ico"></i>Login</span><span class="sep">|</span>
    <span><i class="ico"></i>Sign up</span>
    <svg class="flag" viewBox="0 0 16 11"><rect width="16" height="11" fill="#243b85"/><path d="M0 0L16 11M16 0L0 11" stroke="#fff" stroke-width="2"/><path d="M8 0V11M0 5.5H16" stroke="#fff" stroke-width="3"/><path d="M8 0V11M0 5.5H16" stroke="#cc1f2f" stroke-width="1.6"/></svg>
    <svg class="flag" viewBox="0 0 16 11"><rect width="16" height="11" fill="#fff"/><rect y="3.7" width="16" height="3.7" fill="#1c3fa0"/><rect y="7.3" width="16" height="3.7" fill="#d3212b"/></svg>
    <svg class="flag" viewBox="0 0 16 11"><rect width="16" height="11" fill="#c60b1e"/><rect y="2.8" width="16" height="5.4" fill="#ffc400"/></svg>
    <svg class="flag" viewBox="0 0 16 11"><rect width="16" height="3.7" fill="#000"/><rect y="3.7" width="16" height="3.7" fill="#dd0000"/><rect y="7.3" width="16" height="3.7" fill="#ffce00"/></svg>
    <span class="cart">CART : <b>0 items</b></span>
  </div>
  <div class="brand"><span class="brand-dot"></span><span class="brand-name">Layerhub</span></div>
  <div class="brand-tag">3D PRINTING MARKET</div>
  <nav class="main-nav">
    <a class="active">Home</a><a>3d Product</a><a>Specials</a><a>All Products</a><a>Best Selling</a><a>Faq</a><a style="border:none">Contact Us</a>
  </nav>
</header>

<section class="hero"></section>
<aside class="brand-menu">
  <h3>Shop by Brand</h3>
  <ul>
    <li>Lorem Ipsum Dolor Sit amet</li>
    <li>Iriure&nbsp; in hendrerit here</li>
    <li>Feugiat nulla facilisis dumy</li>
    <li>Tporem Ipsum construct sit</li>
    <li>Lorem Ipsum Dolor Sit</li>
    <li>Iriure&nbsp; in hendrerit amet sit</li>
    <li>Feugiat nulla facilisis sit</li>
  </ul>
</aside>
<div class="search"><span>Search</span><i></i></div>
<div class="printer-photo" role="img" aria-label="Photo of a grey desktop printer"></div>
<h1 class="hero-title">3D PRINTING MARKET</h1>
<ul class="hero-points">
  <li>Lorem ipsum dolor sit amet</li><li>Lpsum dolor sit amet</li><li>Curabitur tincidun</li>
  <li>In vulputat</li><li>Lpsum dolor sit amet</li><li>Curabitur tincidun</li>
</ul>
<div class="learn-more">LEARN MORE<i></i></div>
<div class="dots"><span></span><span></span><span class="on"></span><span></span></div>

<section class="features">
  <div class="feature">
    <div class="feature-icon"><svg width="24" height="18" viewBox="0 0 24 18"><path d="M2 4h14l-3 10H5z" fill="none" stroke="#555" stroke-width="2.5"/><circle cx="7" cy="16" r="1.6" fill="#555"/><circle cx="13" cy="16" r="1.6" fill="#555"/></svg></div>
    <h4>Who We Are ?</h4><p>Lorem ipsum dolor sit amet,<br>consectetur adipiscing elit.<br>adipiscing elit.</p>
  </div>
  <div class="feature">
    <div class="feature-icon"><svg width="22" height="22" viewBox="0 0 22 22"><rect x="2" y="8" width="18" height="5" fill="#555"/><rect x="3.5" y="13" width="15" height="8" fill="#555"/><rect x="10" y="8" width="2" height="13" fill="#fff"/><path d="M11 8C8 2 4 4 7 8M11 8C14 2 18 4 15 8" fill="none" stroke="#555" stroke-width="1.6"/></svg></div>
    <h4>Special</h4><p>Lorem ipsum dolor sit amet,<br>consectetur adipiscing elit.<br>adipiscing elit.</p>
  </div>
  <div class="feature">
    <div class="feature-icon"><svg width="22" height="22" viewBox="0 0 22 22"><path d="M5 2l4 4-2 3c1 3 3 5 6 6l3-2 4 4-3 3C9 20 2 13 2 5z" fill="#555"/></svg></div>
    <h4>24/7 Help</h4><p>Lorem ipsum dolor sit amet,<br>consectetur adipiscing elit.<br>adipiscing elit.</p>
  </div>
  <div class="feature">
    <div class="feature-icon"><svg width="28" height="20" viewBox="0 0 28 20"><rect x="1" y="3" width="18" height="12" fill="#555"/><path d="M19 7h5l3 4v4h-8z" fill="#555"/><circle cx="7" cy="16" r="2.5" fill="#555" stroke="#fff"/><circle cx="22" cy="16" r="2.5" fill="#555" stroke="#fff"/><text x="3" y="12" font-size="6" font-family="Roboto,sans-serif" font-weight="700" fill="#fff">FREE</text></svg></div>
    <h4>Free Shipping</h4><p>Lorem ipsum dolor sit amet,<br>consectetur adipiscing elit.<br>adipiscing elit.</p>
  </div>
</section>

<article class="promo" style="left:93px">
  <h2>Professional 3D<br><em>Printing</em></h2>
  <p>Lorem ipsum dolor sit amet, consectetuer adipiscing elit, sed diam nonummy nibh euismod</p>
  <div class="btn">Read More</div>
  <div class="photo" role="img" aria-label="Photo of a black desktop 3D printer" style="left:155px;top:40px;width:108px;height:86px;background:linear-gradient(160deg,#3a3a3a,#111 70%);border-radius:4px"></div>
</article>
<article class="promo" style="left:376px">
  <h2>Get Affordable<br><em>Services</em></h2>
  <p>Lorem ipsum dolor sit amet, consectetuer adipiscing elit, sed diam nonummy nibh euismod</p>
  <div class="btn">Read More</div>
  <div class="photo" role="img" aria-label="Photo of a smiling business team in suits" style="left:138px;top:43px;width:132px;height:87px;background:linear-gradient(90deg,#3b3430,#d9c2a8 45%,#2f2f36)"></div>
</article>

<div class="section-title"><span>Featured <b>Products</b></span></div>

<svg class="arrow" style="left:66px;top:716px" viewBox="0 0 14 18"><path d="M11 1L3 9l8 8" fill="none" stroke="#555" stroke-width="4"/></svg>
<svg class="arrow" style="left:660px;top:716px" viewBox="0 0 14 18"><path d="M3 1l8 8-8 8" fill="none" stroke="#555" stroke-width="4"/></svg>
<svg class="arrow" style="left:66px;top:879px" viewBox="0 0 14 18"><path d="M11 1L3 9l8 8" fill="none" stroke="#555" stroke-width="4"/></svg>
<svg class="arrow" style="left:660px;top:879px" viewBox="0 0 14 18"><path d="M3 1l8 8-8 8" fill="none" stroke="#555" stroke-width="4"/></svg>

<div class="product" style="left:92px;top:630px"><div class="photo" role="img" aria-label="Photo of a woman holding a colour swatch fan" style="background:linear-gradient(110deg,#f2d7b8,#e47b5c 35%,#777 70%,#eee)"></div><h5>Lorem ipsum dummy text</h5><p>Neque porro quisquam est, qui ipsum quia dolor sit amet</p><div class="price-bar"><span class="price">$299.99</span><span class="add">Add to cart</span></div></div>
<div class="product" style="left:280px;top:630px"><div class="photo" role="img" aria-label="Photo of a decorated gift box on a pink background" style="background:linear-gradient(#e88aa6,#c9414f 60%,#f1c7d0)"></div><h5>Lorem ipsum dummy text</h5><p>Neque porro quisquam est, qui ipsum quia dolor sit amet</p><div class="price-bar"><span class="price">$299.99</span><span class="add">Add to cart</span></div></div>
<div class="product" style="left:468px;top:630px"><div class="photo" role="img" aria-label="Photo of fanned paper samples" style="background:linear-gradient(160deg,#3f3a36,#b8262e 40%,#e7d6bd 70%,#f6f2ea)"></div><h5>Lorem ipsum dummy text</h5><p>Neque porro quisquam est, qui ipsum quia dolor sit amet</p><div class="price-bar"><span class="price">$299.99</span><span class="add">Add to cart</span></div></div>

<div class="product" style="left:92px;top:803px"><div class="photo" role="img" aria-label="Photo of a print studio desk with shirts and colour charts" style="background:linear-gradient(170deg,#f1f1f1,#e5a35a 40%,#333 65%,#e9e9e9)"></div><h5>Lorem ipsum dummy text</h5><p>Neque porro quisquam est, qui ipsum quia dolor sit amet</p><div class="price-bar"><span class="price">$299.99</span><span class="add">Add to cart</span></div></div>
<div class="product" style="left:280px;top:803px"><div class="photo" role="img" aria-label="Photo of fanned paper samples" style="background:linear-gradient(160deg,#3f3a36,#b8262e 40%,#e7d6bd 70%,#f6f2ea)"></div><h5>Lorem ipsum dummy text</h5><p>Neque porro quisquam est, qui ipsum quia dolor sit amet</p><div class="price-bar"><span class="price">$299.99</span><span class="add">Add to cart</span></div></div>
<div class="product" style="left:468px;top:803px"><div class="photo" role="img" aria-label="Photo of a decorated gift box on a pink background" style="background:linear-gradient(#e88aa6,#c9414f 60%,#f1c7d0)"></div><h5>Lorem ipsum dummy text</h5><p>Neque porro quisquam est, qui ipsum quia dolor sit amet</p><div class="price-bar"><span class="price">$299.99</span><span class="add">Add to cart</span></div></div>

<div class="divider"></div>
<div class="more-info">More Information?</div>
<div class="more-sub">Contact Layerhub Now</div>
<svg class="abs" style="left:303px;top:987px" width="18" height="22" viewBox="0 0 22 22"><path d="M5 2l4 4-2 3c1 3 3 5 6 6l3-2 4 4-3 3C9 20 2 13 2 5z" fill="#2b8fd6"/></svg>
<div class="phone-number">123-456-7890</div>
<div class="contact-btn">CONTACT US NOW</div>

<footer class="site-footer">
  <div class="fcol" style="left:92px"><h4>Company Info</h4><ul><li>Home</li><li>3D Product</li><li>Specials</li><li>All Products</li><li>Best Selling</li><li>Faq</li><li>Contact</li></ul></div>
  <div class="fcol" style="left:202px"><h4>Customer Service</h4><ul><li>Contact Us</li><li>Nunc consequat purus vel enim</li><li>Etiam sagittis ante</li><li>Aenean sollicitudin mauris</li><li>Nunc consequat purus</li><li>Pellentesque convallis</li><li>Cras gravida purus vitae</li></ul></div>
  <div class="fcol countries" style="left:361px"><h4>Layerhub</h4>
    <ul><li>Austria</li><li>Brazil</li><li>France</li><li>Germany</li><li>Indonesia</li><li>Japan</li><li>Malaysia</li><li>Spain</li></ul><ul><li>Austria</li><li>Brazil</li><li>France</li><li>Germany</li><li>Indonesia</li><li>Japan</li><li>Malaysia</li><li>Spain</li></ul>
  </div>
  <div class="alerts">
    <span class="bell"></span>
    <h4>Layerhub<br><b>Alerts</b></h4>
    <p>Get weekly updates on promotions and coupons</p>
    <div class="signup"><span>Email address</span><b>SIGNUP</b></div>
    <div class="social">
      <span style="background:#3b5998">Fr</span><span style="background:#29a9e1">Ch</span><span style="background:#0b77b5">Lk</span><span style="background:#f7941d">Fd</span>
    </div>
  </div>
  <div class="foot-line"></div>
  <div class="payments"><span class="label">Payment Options :</span>
    <span class="pay">Paywell</span><span class="pay">Cardiva</span><span class="pay" style="background:#1a3f8a;color:#fff">C.Volt</span><span class="pay" style="background:#263a7a;color:#fff">Orbicard</span><span class="pay" style="background:#263a7a;color:#fff">Dirigo</span>
  </div>
  <div class="copyright">Copyright © 2013, Layerhub. All Rights Reserved</div>
</footer>

</body>
</html>
```